Brightfield Steel Depot (Metal Roofing Manufacturing and Supply) needs a billboard design

We need a billboard design for for our metal roofing manufacturing company in Sarasota FL, Brightfield Steel Depot Inc. You can visit our website www.brightfieldsteeldepot-example.com for more info about our company. We located are off Exit 210 on I 75- 482 Pinegrove Rd. Sarasota 34019
The billboard will be on I75 north of our office

I have a design that I am interested in but waiting on minor corrections from designer

```html
<!DOCTYPE html>
<html lang="en">
<head>
<meta charset="utf-8">
<title>Brightfield Steel Depot – Billboard</title>
<link rel="stylesheet" href="https://fonts.googleapis.com/css2?family=Arimo:wght@700&family=Orbitron:wght@900&display=swap">
<style>
  :root {
    --backdrop: #2f5f9a;
    --frame: #8e9296;
    --sky-top: #a9d6f5;
    --sky-bottom: #f2f9fd;
    --roof-dark: #7f9fb3;
    --roof-mid: #a9c1cf;
    --roof-light: #d4e2ea;
    --strip-top: #e6e8ea;
    --strip-bottom: #a3a7ab;
    --band-yellow: #fff200;
    --brand-blue: #0a4fe0;
    --headline-ink: #141414;
  }
  * { margin: 0; padding: 0; box-sizing: border-box; }
  html, body { width: 1200px; height: 675px; overflow: hidden; }
  body {
    background: var(--backdrop);
    position: relative;
  }
  .billboard {
    position: absolute;
    left: 20px;
    top: 165px;
    width: 1160px;
    height: 345px;
    border: 5px solid var(--frame);
    background: var(--sky-bottom);
    overflow: hidden;
  }
  .billboard__sky {
    position: absolute;
    left: 0; top: 0;
    width: 100%; height: 72px;
    background: linear-gradient(to bottom, var(--sky-top), var(--sky-bottom));
  }
  .billboard__headline {
    position: absolute;
    top: 12px;
    left: 240px;
    width: 820px;
    text-align: center;
    font-family: "Orbitron", sans-serif;
    font-weight: 900;
    font-size: 44px;
    letter-spacing: 3px;
    color: var(--headline-ink);
    transform: skewX(-14deg);
    line-height: 1;
  }
  .billboard__roof {
    position: absolute;
    left: 0; top: 72px;
    width: 100%; height: 192px;
    background: linear-gradient(100deg, var(--roof-mid) 0%, var(--roof-dark) 35%, var(--roof-mid) 60%, var(--roof-light) 100%);
  }
  .billboard__brand {
    position: absolute;
    top: 140px;
    left: 40px;
    right: 30px;
    display: flex;
    align-items: center;
    gap: 18px;
  }
  .brand-dot {
    flex: 0 0 auto;
    width: 60px;
    height: 60px;
    border-radius: 50%;
    background: var(--band-yellow);
  }
  .brand-name {
    font-family: "Arimo", Arial, sans-serif;
    font-weight: 700;
    font-size: 78px;
    line-height: 1;
    color: var(--brand-blue);
    white-space: nowrap;
    letter-spacing: -1px;
  }
  .billboard__strip {
    position: absolute;
    left: 0; top: 264px;
    width: 100%; height: 16px;
    background: linear-gradient(to bottom, var(--strip-top), var(--strip-bottom));
  }
  .billboard__tagline-band {
    position: absolute;
    left: 0; top: 280px;
    width: 100%; height: 55px;
    background: var(--band-yellow);
    display: flex;
    align-items: center;
    justify-content: center;
  }
  .tagline {
    font-family: "Arimo", Arial, sans-serif;
    font-weight: 700;
    font-size: 46px;
    letter-spacing: 3px;
    color: var(--brand-blue);
    line-height: 1;
  }
</style>
</head>
<body>
  <main class="billboard">
    <div class="billboard__sky"></div>
    <h2 class="billboard__headline">METAL ROOFING FAST</h2>
    <div class="billboard__roof" role="img" aria-label="Close-up photo of silver standing-seam metal roof panels"></div>
    <h1 class="billboard__brand">
      <span class="brand-dot" aria-hidden="true"></span>
      <span class="brand-name">Brightfield Steel Depot</span>
    </h1>
    <div class="billboard__strip"></div>
    <div class="billboard__tagline-band">
      <p class="tagline">Need your metal roof tomorrow?</p>
    </div>
  </main>
</body>
</html>
```